Rocket business card

Modern business card design, use of color is good with clean space too.

Things to include on card:

Quote: I add fuel to your optometry practice

- Eyewear Sales
- Admin Duties
- Revenue Collection
- Leadership
- Tech Adoption
- COGS Reduction
- Product Sourcing
-Medical Growth

Dalton Vessey, CEO
Glint Harbor
Text Me! 847-302-1964
dalton@glintharbor.example

```html
<!DOCTYPE html>
<html lang="en">
<head>
<meta charset="utf-8">
<title>Glint Harbor – Business Card</title>
<link href="https://fonts.googleapis.com/css2?family=Ubuntu:wght@400;500;700&display=swap" rel="stylesheet">
<style>
  :root {
    --red: #d9392c;
    --orange: #e88e2c;
    --accent: #e8862a;
    --ink: #1b1b1b;
    --paper: #ffffff;
    --stage: #ecebe8;
    --strip: #1f1a17;
  }
  * { box-sizing: border-box; margin: 0; padding: 0; }
  html, body { width: 1200px; height: 1000px; overflow: hidden; }
  body {
    background: var(--stage);
    font-family: "Ubuntu", sans-serif;
    display: flex;
    align-items: center;
    justify-content: center;
    gap: 40px;
  }
  .card {
    position: relative;
    width: 540px;
    height: 310px;
    overflow: hidden;
    box-shadow: 0 6px 18px rgba(0,0,0,0.15);
  }

  /* Front */
  .card-front {
    background: linear-gradient(90deg, var(--red), var(--orange));
    color: var(--paper);
    border-bottom: 9px solid var(--strip);
  }
  .brand {
    display: flex;
    align-items: center;
    gap: 12px;
    font-weight: 500;
    letter-spacing: 0.06em;
    text-transform: uppercase;
  }
  .brand-dot { border-radius: 50%; flex: none; }
  .card-front .brand {
    position: absolute;
    top: 78px;
    left: 0; right: 0;
    justify-content: center;
    font-size: 38px;
    color: var(--paper);
  }
  .card-front .brand-dot { width: 34px; height: 34px; background: var(--paper); }
  .services {
    position: absolute;
    top: 192px;
    left: 0; right: 0;
    display: flex;
    justify-content: center;
    font-size: 12.5px;
    font-weight: 500;
    line-height: 1.35;
  }
  .services ul { list-style: none; padding: 0 9px; }
  .services-left { text-align: right; border-right: 1px solid var(--paper); }
  .services-left li::before { content: "\25B8\00a0"; font-size: 10px; }
  .services-right li::after { content: "\00a0\25C2"; font-size: 10px; }

  /* Back */
  .card-back {
    background: var(--paper);
    color: var(--ink);
    border-bottom: 9px solid var(--accent);
  }
  .card-back .brand {
    position: absolute;
    top: 128px;
    left: 28px;
    font-size: 24px;
    color: var(--ink);
    gap: 10px;
  }
  .card-back .brand-dot { width: 26px; height: 26px; background: var(--accent); }
  .divider {
    position: absolute;
    left: 280px;
    top: 72px;
    width: 2px;
    height: 148px;
    background: var(--accent);
  }
  .contact {
    position: absolute;
    left: 301px;
    top: 100px;
  }
  .contact-name { color: var(--accent); font-weight: 700; font-size: 24px; }
  .contact-role { font-size: 13px; font-weight: 500; margin-top: 2px; }
  .contact-line { font-size: 15px; font-weight: 500; margin-top: 4px; }
  .contact-line:first-of-type { margin-top: 24px; }
  .text-me { color: var(--accent); font-weight: 700; }
</style>
</head>
<body>
  <section class="card card-front" aria-label="Business card front">
    <div class="brand"><span class="brand-dot"></span>Glint Harbor</div>
    <div class="services">
      <ul class="services-left">
        <li>Eyewear Sales</li>
        <li>Admin Duties</li>
        <li>Revenue Collection</li>
        <li>Leadership</li>
      </ul>
      <ul class="services-right">
        <li>Tech Adoption</li>
        <li>COGS Reduction</li>
        <li>Product Sourcing</li>
        <li>Medical Growth</li>
      </ul>
    </div>
  </section>

  <section class="card card-back" aria-label="Business card back">
    <div class="brand"><span class="brand-dot"></span>Glint Harbor</div>
    <div class="divider"></div>
    <div class="contact">
      <p class="contact-name">Dalton Vessey</p>
      <p class="contact-role">CEO</p>
      <p class="contact-line"><span class="text-me">Text Me!</span> 847-302-1964</p>
      <p class="contact-line">dalton@glintharbor.example</p>
    </div>
  </section>
</body>
</html>
```